Birch Flooring Supply

Basic one-sided business card design using the attached logo. Vintage americana theme. Font is modified Arial Nova Cond, but anything that coordinates can be used

```html
<!DOCTYPE html>
<html lang="en">
<head>
<meta charset="utf-8">
<title>Birch Flooring Supply – Business Card</title>
<link href="https://fonts.googleapis.com/css2?family=Arimo:wght@400;700&display=swap" rel="stylesheet">
<style>
  :root {
    --bg: #1b1c1e;
    --card-dark: #262626;
    --gold-light: #c9a27c;
    --gold-mid: #bb9064;
    --gold-deep: #b0804c;
    --gold-text: #c49a6a;
    --ink: #262322;
    --white: #ffffff;
    --edge: #b8956a;
  }
  * { box-sizing: border-box; margin: 0; padding: 0; }
  html, body { width: 1200px; height: 840px; overflow: hidden; background: var(--bg); }
  body { font-family: "Arimo", Arial, sans-serif; position: relative; }

  .card {
    position: absolute;
    width: 540px;
    height: 309px;
    border-radius: 24px;
    box-shadow: 0 18px 40px rgba(0,0,0,0.55);
  }

  /* Back side */
  .card-back {
    left: 110px;
    top: 100px;
    background: linear-gradient(35deg, var(--gold-deep) 0%, var(--gold-mid) 35%, var(--gold-light) 75%);
    display: flex;
    align-items: center;
    justify-content: center;
    gap: 16px;
  }
  .back-mark {
    width: 30px; height: 30px;
    border: 4px solid var(--ink);
    border-radius: 50%;
  }
  .back-name {
    font-weight: 700;
    font-size: 30px;
    color: var(--ink);
    text-transform: uppercase;
    letter-spacing: 1px;
  }

  /* Front side */
  .card-front {
    left: 550px;
    top: 440px;
    background: var(--card-dark);
    border-bottom: 4px solid var(--edge);
    border-right: 2px solid var(--edge);
    overflow: hidden;
  }
  .front-name {
    position: absolute;
    left: 130px;
    top: 62px;
    width: 380px;
    font-weight: 700;
    font-size: 32px;
    line-height: 1.1;
    color: var(--white);
    text-transform: uppercase;
    letter-spacing: 1px;
  }
  .person {
    position: absolute;
    left: 40px;
    top: 168px;
    width: 220px;
    text-align: right;
  }
  .person-name {
    font-size: 22px;
    font-weight: 400;
    color: var(--gold-text);
    text-transform: uppercase;
  }
  .person-role {
    font-size: 15px;
    color: var(--white);
    margin-top: 2px;
  }
  .divider {
    position: absolute;
    left: 278px;
    top: 160px;
    width: 1px;
    height: 76px;
    background: rgba(255,255,255,0.7);
  }
  .contacts {
    position: absolute;
    left: 296px;
    top: 160px;
    list-style: none;
  }
  .contacts li {
    display: flex;
    align-items: center;
    gap: 8px;
    font-size: 15px;
    color: var(--white);
    height: 25px;
  }
  .contacts svg { width: 13px; height: 13px; flex: none; }
  .address {
    position: absolute;
    left: 0; right: 0;
    top: 256px;
    text-align: center;
    font-size: 15px;
    color: var(--white);
  }
</style>
</head>
<body>
  <section class="card card-back" aria-label="Business card back">
    <span class="back-mark"></span>
    <span class="back-name">Birch Flooring Supply</span>
  </section>

  <section class="card card-front" aria-label="Business card front">
    <div class="front-name">Birch Flooring Supply</div>

    <div class="person">
      <div class="person-name">Daniel Harper</div>
      <div class="person-role">Manager</div>
    </div>

    <div class="divider"></div>

    <ul class="contacts">
      <li>
        <svg viewBox="0 0 24 24" fill="none" stroke="#c49a6a" stroke-width="2.4"><path d="M5 3h4l2 5-3 2a12 12 0 0 0 6 6l2-3 5 2v4a2 2 0 0 1-2 2A18 18 0 0 1 3 5a2 2 0 0 1 2-2z"/></svg>
        555-014-2100
      </li>
      <li>
        <svg viewBox="0 0 24 24" fill="none" stroke="#c49a6a" stroke-width="2.4"><rect x="2" y="5" width="20" height="14" rx="1"/><path d="M2 6l10 7 10-7"/></svg>
        dharper@birchfloors.com
      </li>
      <li>
        <svg viewBox="0 0 24 24" fill="none" stroke="#c49a6a" stroke-width="2.2"><circle cx="12" cy="12" r="10"/><path d="M2 12h20M12 2c3 3 3 17 0 20M12 2c-3 3-3 17 0 20"/></svg>
        www.birchfloors.com
      </li>
    </ul>

    <div class="address">Your Address, City, State, Zip 0000</div>
  </section>
</body>
</html>
```